Brimvale Crest Homes needs a business card

We need a business card for a new company in Canada, Ontario. Our company is all about luxury contraction homes for our clients. Our product and services are custom projects design. Under the business logo that will be created, we want a slogan that will be a memorable phrase for consumers to remember us to tell their friends and relatives.

Additional infomation
- Teodoro Vanlesky
- President / Ceo
-519.304.7718

Find point what luxury construction products and services can be done

We like to see colors:
- #663300
- and something other colors or color that would attract the client needs and wants

The final design should communicate leads from new or old clients that will grow our empire. Most of all, we try to work among the budget that clients want

NOTE
- we also need an icon for the business (Example: Instagram, Facebook, and Whatsapp icons)
- We want the company name to be remembered easily for clients and our distributors who would get our orders.
- we need an icon on the business cards: Facebook and Instagram.

Thanks,
Brimvale Crest Homes

```html
<!DOCTYPE html>
<html lang="en">
<head>
<meta charset="utf-8">
<title>Brimvale Crest Homes – Business Card</title>
<link rel="stylesheet" href="https://fonts.googleapis.com/css2?family=Oswald:wght@500;700&family=Poppins:wght@400;500&display=swap">
<style>
  :root {
    --brand-brown: #663300;
    --ink-grey: #555555;
    --card-white: #ffffff;
    --backdrop: #e6e4e1;
    --rule-grey: #9a9a9a;
  }
  * { margin: 0; padding: 0; box-sizing: border-box; }
  html, body { width: 1200px; height: 874px; overflow: hidden; }
  body {
    background: var(--backdrop);
    position: relative;
  }
  .card {
    position: absolute;
    left: 250px;
    width: 700px;
    height: 380px;
    background: var(--card-white);
    box-shadow: 0 6px 18px rgba(0,0,0,0.12);
  }
  .card--front { top: 40px; }
  .card--back { top: 454px; }

  .wordmark {
    font-family: "Oswald", sans-serif;
    font-weight: 700;
    color: var(--brand-brown);
    letter-spacing: 0.5px;
    line-height: 1;
    white-space: nowrap;
  }
  .tagline {
    font-family: "Oswald", sans-serif;
    font-weight: 500;
    color: var(--brand-brown);
    text-transform: uppercase;
    letter-spacing: 0.6px;
    white-space: nowrap;
  }

  /* Front */
  .front-brand {
    position: absolute;
    top: 120px;
    left: 0;
    width: 100%;
    text-align: center;
  }
  .front-brand .wordmark { font-size: 52px; }
  .front-brand .tagline { font-size: 17px; margin-top: 8px; }
  .social-row {
    position: absolute;
    top: 292px;
    left: 0;
    width: 100%;
    display: flex;
    justify-content: center;
    gap: 6px;
  }
  .social-row svg { width: 30px; height: 30px; }

  /* Back */
  .back-brand {
    position: absolute;
    top: 150px;
    left: 36px;
    width: 300px;
    text-align: center;
  }
  .back-brand .wordmark { font-size: 34px; }
  .back-brand .tagline { font-size: 11.5px; margin-top: 6px; }
  .divider {
    position: absolute;
    top: 120px;
    left: 372px;
    width: 2px;
    height: 140px;
    background: linear-gradient(to bottom, rgba(154,154,154,0), var(--rule-grey) 50%, rgba(154,154,154,0));
  }
  .contact {
    position: absolute;
    top: 150px;
    left: 400px;
    font-family: "Poppins", sans-serif;
  }
  .contact__name {
    font-size: 24px;
    font-weight: 500;
    color: var(--brand-brown);
    letter-spacing: 0.5px;
  }
  .contact__role {
    font-size: 19px;
    color: var(--ink-grey);
    margin-top: 2px;
  }
  .contact__phone {
    font-size: 17px;
    color: var(--ink-grey);
    margin-top: 4px;
  }
</style>
</head>
<body>
  <section class="card card--front" aria-label="Business card front">
    <div class="front-brand">
      <div class="wordmark">Brimvale Crest Homes</div>
      <div class="tagline">- Home Renovations - Custom Project Design -</div>
    </div>
    <div class="social-row" aria-label="Social media links">
      <svg viewBox="0 0 30 30" aria-hidden="true"><circle cx="15" cy="15" r="13.5" fill="none" stroke="var(--brand-brown)" stroke-width="1.2"/></svg>
      <svg viewBox="0 0 30 30" aria-hidden="true"><circle cx="15" cy="15" r="13.5" fill="none" stroke="var(--brand-brown)" stroke-width="1.2"/></svg>
      <svg viewBox="0 0 30 30" aria-hidden="true"><circle cx="15" cy="15" r="13.5" fill="none" stroke="var(--brand-brown)" stroke-width="1.2"/></svg>
    </div>
  </section>

  <section class="card card--back" aria-label="Business card back">
    <div class="back-brand">
      <div class="wordmark">Brimvale Crest Homes</div>
      <div class="tagline">- Home Renovations - Custom Project Design -</div>
    </div>
    <div class="divider"></div>
    <div class="contact">
      <div class="contact__name">Teodoro Vanlesky</div>
      <div class="contact__role">President / Ceo</div>
      <div class="contact__phone">519.304.7718</div>
    </div>
  </section>
</body>
</html>
```